Presentation Template for Copperline Ventures

We would like to have a template for our presentations since we have a new logo and want a new general image.

The new template should have as minimum Cover/Title Page, Bullets page and Regular page. We have a new logo and need the template to mach with it. For the bullets and regular page we want the design no take much part for including content, so we would like something that makes the slides look good but leaving most of room free for writing.

We would like the logo on the footer of the regular slides (not of course for the cover, dividers etc)

I'm attaching de logo here. Our logo colours are #b80016, #006ac6 and black

Thank you

Industry/Entity Type

It Company

Font styles to use
Other font styles liked:
• Maven Pro

Colors
ec1f27
0355a3
000000

Requirements
Must have
• Presentation template with Cover/Title Page, Bullets page and Regular page. Must match with our new logo.
• We would like the logo on the footer of the regular slides (not of course for the cover, dividers etc)
• Our logo colours are #b80016, #006ac6 and black
Nice to have
• Other type of slides, special bullets etc
Should not have
• I don't know

```html
<!DOCTYPE html>
<html lang="en">
<head>
<meta charset="utf-8">
<title>Copperline Ventures — Presentation Template</title>
<link href="https://fonts.googleapis.com/css2?family=Roboto:wght@300;400;700;900&family=Maven+Pro:wght@400;700&display=swap" rel="stylesheet">
<style>
:root{
  --blue:#0a62c4;
  --blue-dark:#0355a3;
  --blue-soft:#3f86d6;
  --red:#c8102e;
  --ink:#222;
  --grey:#8e8e8e;
  --grey-panel:#9a9a9a;
  --sheet:#ebebeb;
  --white:#fff;
}
*{box-sizing:border-box;margin:0;padding:0}
html,body{width:1200px;height:900px;overflow:hidden;background:var(--sheet);font-family:"Roboto",sans-serif;color:var(--ink)}
.sheet{position:relative;width:1200px;height:900px}
.slide{position:absolute;width:293px;height:166px;background:var(--white);overflow:hidden;box-shadow:0 1px 3px rgba(0,0,0,.12)}
.c1{left:134px}.c2{left:433px}.c3{left:732px}
.r1{top:21px}.r2{top:191px}.r3{top:361px}.r4{top:531px}.r5{top:701px}
.abs{position:absolute}
.slide-title{position:absolute;left:11px;top:11px;font-weight:300;font-size:8.5px;color:var(--blue);letter-spacing:-.1px}
.slide-sub{position:absolute;left:11px;top:23px;font-size:3.6px;color:var(--grey);text-transform:uppercase}
.body{font-size:3.4px;line-height:1.55;color:#333;text-align:justify}
.lead{font-weight:700;color:var(--blue);font-size:3.6px;display:block}
.lead.red{color:var(--red)}
.photo{position:absolute}
.brand{font-family:"Maven Pro",sans-serif;font-weight:700;color:var(--red);letter-spacing:.4px;white-space:nowrap;display:flex;align-items:center}
.brand i{display:inline-block;background:var(--red)}
.foot{position:absolute;left:0;bottom:0;width:293px;height:14px}
.foot .brand{position:absolute;left:6px;top:1px;font-size:3.4px}
.foot .brand i{width:5px;height:5px;margin-right:2px}
.foot svg{position:absolute;left:0;bottom:0}
.foot .pg{position:absolute;right:4px;bottom:2.5px;font-size:2.8px;color:var(--white)}
.heading-white{color:var(--white)}
.toc-item{position:absolute;display:flex;align-items:center;gap:4px;font-size:3.4px;font-weight:700;color:var(--white);line-height:1.4}
.toc-num{width:9px;height:9px;border-radius:50%;background:rgba(255,255,255,.35);border:1px solid rgba(255,255,255,.7);font-size:3.4px;display:flex;align-items:center;justify-content:center}
.tile{position:absolute;width:73px;padding:20px 6px 0;font-size:3.3px;font-weight:700;line-height:1.4;color:var(--white)}
.tile.blue{background:var(--blue)}
.tile.grey{background:var(--grey-panel)}
.svc{position:absolute;width:61px;color:var(--white);text-align:center}
.svc-head{height:36px;display:flex;flex-direction:column;align-items:center;justify-content:flex-end;padding-bottom:2px;font-size:3.4px;font-weight:700;line-height:1.2}
.svc-body{margin-top:1.5px;height:51px;padding:5px 4px;font-size:3px;font-weight:700;line-height:1.45}
.fill-blue{background:var(--blue)}
.fill-grey{background:var(--grey-panel)}
.sol{position:absolute;width:70px;height:34px;border:.8px solid var(--blue);padding:3px 4px;font-size:3px;line-height:1.4}
.sol b{display:block;font-size:3.6px;font-weight:400;margin-bottom:2px}
.sol.on{background:var(--blue);color:var(--white)}
.sol.on span{font-weight:700}
.sol.off{color:#333}
.sol.off b{color:var(--blue)}
.bullet{position:absolute;left:58px;width:206px}
.bullet .lead::before{content:"➔ ";color:var(--red)}
.member{position:absolute;width:62px;text-align:center}
.avatar{width:23px;height:23px;border-radius:50%;margin:0 auto 4px;border:1.5px solid var(--blue);background:radial-gradient(circle at 50% 40%,#d9d9d9,#777)}
.member .name{font-size:3.4px;font-weight:700;color:var(--red)}
.member .role{font-size:2.6px;font-style:italic;color:#555;margin-bottom:4px}
.member .body{text-align:center}
.donut{position:absolute;width:62px;text-align:center}
.donut .body{text-align:center;margin-top:4px}
.contact{position:absolute;left:28px;display:flex;align-items:center;gap:4px;font-size:3.6px;color:var(--white)}
.contact i{width:6px;height:6px;border-radius:50%;background:var(--white);display:inline-block}
</style>
</head>
<body>
<main class="sheet">

<!-- Cover -->
<section class="slide c1 r1">
  <div class="brand abs" style="left:16px;top:37px;font-size:5px"><i style="width:11px;height:11px;margin-right:3px"></i>COPPERLINE<br>VENTURES</div>
  <div class="photo" role="img" aria-label="Hand touching a digital hexagon network interface" style="left:0;top:60px;width:293px;height:67px;background:linear-gradient(90deg,#5d86b6,#c9d6e6 45%,#6f97c8)"></div>
  <svg class="abs" style="left:0;top:50px" width="293" height="78" viewBox="0 0 293 78">
    <path d="M120 78 C150 78 150 22 185 12 L293 0 L293 78 Z" fill="var(--blue)"/>
    <path d="M0 10 L120 10 C140 10 150 4 170 0 L0 0 Z" fill="var(--white)"/>
  </svg>
  <div class="abs heading-white" style="right:16px;top:62px;text-align:right">
    <div style="font-family:'Roboto',sans-serif;font-size:13px;font-weight:400;letter-spacing:-.3px">WELCOME</div>
    <div style="font-size:6.5px;font-weight:300;letter-spacing:1.4px;margin-top:1px">TO OUR PRESENTATION</div>
    <div style="font-size:3.6px;margin-top:5px">Newyork, March 25, 2017</div>
  </div>
  <div class="abs" style="left:28px;top:143px;font-size:2.6px;color:#555;line-height:1.4">© 2017 All rights reserved. Contents confidential and proprietary information and may not be disclosed or<br>reproduced without the prior written consent of Copperline Ventures.</div>
  <div class="abs" style="left:0;bottom:0;width:293px;height:3px;background:var(--red)"></div>
</section>

<!-- Table of contents -->
<section class="slide c2 r1" style="background:var(--blue)">
  <div class="photo" role="img" aria-label="Faint cloud and technology icons over blue" style="inset:0;background:radial-gradient(circle at 60% 35%,rgba(255,255,255,.22),transparent 55%),linear-gradient(135deg,var(--blue),#2f7fd6)"></div>
  <div class="abs heading-white" style="left:31px;top:44px">
    <div style="font-size:4.5px">TABLE OF</div>
    <div style="font-size:10px;font-weight:300">CONTENTS</div>
  </div>
  <div class="toc-item" style="left:48px;top:84px"><span class="toc-num">1</span><span>LOREM IPSUM DOLOR SIT<br>MET DOLOR SIT MET</span></div>
  <div class="toc-item" style="left:48px;top:106px"><span class="toc-num">1</span><span>LOREM IPSUM DOLOR SIT<br>MET DOLOR SIT MET</span></div>
  <div class="toc-item" style="left:48px;top:127px"><span class="toc-num">1</span><span>LOREM IPSUM DOLOR SIT<br>MET DOLOR SIT MET</span></div>
  <div class="toc-item" style="left:152px;top:84px"><span class="toc-num">1</span><span>LOREM IPSUM DOLOR SIT<br>MET DOLOR SIT MET</span></div>
  <div class="toc-item" style="left:152px;top:106px"><span class="toc-num">1</span><span>LOREM IPSUM DOLOR SIT<br>MET DOLOR SIT MET</span></div>
  <div class="toc-item" style="left:152px;top:127px"><span class="toc-num">1</span><span>LOREM IPSUM DOLOR SIT<br>MET DOLOR SIT MET</span></div>
</section>

<!-- About us 1 -->
<section class="slide c3 r1">
  <h2 class="slide-title">ABOUT US</h2><p class="slide-sub">Subtitle goes here</p>
  <div class="abs heading-white" style="left:0;top:41px;width:95px;height:54px;background:var(--blue);padding:18px 12px 0;font-size:3.4px;font-weight:700;line-height:1.5">LOREM IPSUM DOLOR SIT MET CONSECTUR ADIPISCING ELIT, SED DO EIUSMOD TEMPOR INCIDIDUNT UT LABORE ET DOLORE MAGNA</div>
  <div class="photo" role="img" aria-label="Team of colleagues in a bright office" style="left:95px;top:41px;width:198px;height:54px;background:linear-gradient(90deg,#bfbfbf,#efefef 50%,#a9a9a9)"></div>
  <div class="abs body" style="left:95px;top:101px;width:182px">Lorem ipsum dolor sit amet, consectetur adipiscing elit, sed do eiusmod tempor incididunt ut labore et dolore magna aliqua. Ut enim ad minim veniam, quis nostrud exercitation ullamco laboris nisi ut aliquip ex ea commodo consequat. Duis aute irure dolor in reprehenderit in voluptate velit esse cillum dolore eu fugiat nulla pariatur.<br><br>Lorem ipsum dolor sit amet, consectetur adipiscing elit, sed do eiusmod tempor incididunt ut labore et dolore magna aliqua. Ut enim ad minim veniam, quis nostrud exercitation ullamco laboris nisi ut aliquip ex ea commodo consequat.</div>
  <div class="foot"><span class="brand"><i></i>COPPERLINE VENTURES</span><svg width="293" height="8" viewBox="0 0 293 8"><polygon points="218,8 226,2 293,2 293,8" fill="var(--blue)"/><rect y="6" width="293" height="2" fill="var(--red)"/></svg><span class="pg">02</span></div>
</section>

<!-- About us 2 -->
<section class="slide c1 r2">
  <h2 class="slide-title">ABOUT US</h2><p class="slide-sub">Subtitle goes here</p>
  <div class="photo" role="img" aria-label="Business people with digital devices" style="left:15px;top:49px;width:60px;height:36px;background:linear-gradient(135deg,#d4e0ef,#6b8fbd)"></div>
  <div class="abs" style="left:15px;top:90px;width:60px;text-align:right;font-size:3.4px;font-weight:700;color:var(--red);line-height:1.5">Lorem ipsum dolor sit amet<br>consectetur adipiscing<br>elit sed do eiusmod</div>
  <div class="abs body" style="left:88px;top:48px;width:98px"><span class="lead">Lorem ipsum dolor sit amet</span>consectetur adipiscing elit, sed do eiusmod tempor incididunt ut labore et dolore magna aliqua. Ut enim ad minim veniam, quis nostrud exercitation ullamco laboris nisi ut aliquip ex ea commodo consequat. Duis aute irure dolor in reprehenderit in voluptate velit esse cillum dolore eu fugiat nulla pariatur.<br><span class="lead" style="margin-top:3px">Lorem ipsum dolor sit amet</span>consectetur adipiscing elit, sed do eiusmod tempor incididunt ut labore et dolore magna aliqua. Ut enim ad minim veniam, quis nostrud exercitation ullamco laboris nisi ut aliquip ex ea</div>
  <div class="abs body" style="left:186px;top:48px;width:96px"><span class="lead">Lorem ipsum dolor sit amet</span>consectetur adipiscing elit, sed do eiusmod tempor incididunt ut labore et dolore magna aliqua. Ut enim ad minim veniam, quis nostrud exercitation ullamco laboris nisi ut aliquip ex ea commodo consequat. Duis aute irure dolor in reprehenderit in voluptate velit esse cillum dolore eu fugiat nulla pariatur.<br><span class="lead" style="margin-top:3px">Lorem ipsum dolor sit amet</span>consectetur adipiscing elit, sed do eiusmod tempor incididunt ut labore et dolore magna aliqua. Ut enim ad minim veniam, quis nostrud exercitation ullamco laboris nisi ut aliquip ex ea</div>
  <div class="foot"><span class="brand"><i></i>COPPERLINE VENTURES</span><svg width="293" height="8" viewBox="0 0 293 8"><polygon points="218,8 226,2 293,2 293,8" fill="var(--blue)"/><rect y="6" width="293" height="2" fill="var(--red)"/></svg><span class="pg">02</span></div>
</section>

<!-- About us 3: tile grid -->
<section class="slide c2 r2">
  <h2 class="slide-title">ABOUT US</h2><p class="slide-sub">Subtitle goes here</p>
  <div class="photo" role="img" aria-label="Business team reviewing documents" style="left:0;top:36px;width:73px;height:45px;background:linear-gradient(135deg,#e6ecf4,#55627a)"></div>
  <div class="tile blue" style="left:73px;top:36px;height:45px">LOREM IPSUM DOLOR SIT MET CONSECTUR ADIPISCING ELIT, SED DO EIUSMOD TEMPOR INC IDIDUNT UT LABORE ET</div>
  <div class="photo" role="img" aria-label="Hand touching automation interface" style="left:146px;top:36px;width:73px;height:45px;background:linear-gradient(135deg,#c7d4e4,#3c5679)"></div>
  <div class="tile blue" style="left:219px;top:36px;height:45px;width:74px">LOREM IPSUM DOLOR SIT MET CONSECTUR ADIPISCING ELIT, SED DO EIUSMOD TEMPOR INC IDIDUNT UT LABORE ET</div>
  <div class="tile grey" style="left:0;top:81px;height:52px">LOREM IPSUM DOLOR SIT MET CONSECTUR ADIPISCING ELIT, SED DO EIUSMOD TEMPOR INC IDIDUNT UT LABORE ET</div>
  <div class="photo" role="img" aria-label="Finger pressing a glowing digital button" style="left:73px;top:81px;width:73px;height:52px;background:radial-gradient(circle at 50% 50%,#4f8fd0,#1a2c46)"></div>
  <div class="tile grey" style="left:146px;top:81px;height:52px">LOREM IPSUM DOLOR SIT MET CONSECTUR ADIPISCING ELIT, SED DO EIUSMOD TEMPOR INC IDIDUNT UT LABORE ET</div>
  <div class="photo" role="img" aria-label="Medical technology icons on a screen" style="left:219px;top:81px;width:74px;height:52px;background:linear-gradient(135deg,#e9f2f7,#8fc0d3)"></div>
  <div class="foot"><span class="brand"><i></i>COPPERLINE VENTURES</span><svg width="293" height="8" viewBox="0 0 293 8"><polygon points="218,8 226,2 293,2 293,8" fill="var(--blue)"/><rect y="6" width="293" height="2" fill="var(--red)"/></svg><span class="pg">02</span></div>
</section>

<!-- About us 4: three photos -->
<section class="slide c3 r2">
  <h2 class="slide-title">ABOUT US</h2><p class="slide-sub">Subtitle goes here</p>
  <div class="photo" role="img" aria-label="Hands holding a glowing globe" style="left:35px;top:45px;width:70px;height:47px;background:radial-gradient(circle at 50% 50%,#7fb6ea,#1c3558)"></div>
  <div class="photo" role="img" aria-label="Business team gathered around a table" style="left:112px;top:45px;width:70px;height:47px;background:linear-gradient(135deg,#a8c7a0,#2d4a6b)"></div>
  <div class="photo" role="img" aria-label="Hand touching a digital interface" style="left:189px;top:45px;width:70px;height:47px;background:radial-gradient(circle at 50% 50%,#d58a4a,#242424)"></div>
  <div class="abs body" style="left:35px;top:96px;width:70px"><span class="lead" style="margin-bottom:3px">Lorem ipsum dolor sit amet</span>Ut enim ad minim veniam, quis nostrud exercitation ullamco laboris nisi ut aliquip ex ea commodo consequat. Duis aute irure dolor in reprehenderit in voluptate velit esse cillum dolore eu fugiat nulla pariatur.</div>
  <div class="abs body" style="left:112px;top:96px;width:70px"><span class="lead" style="margin-bottom:3px">Lorem ipsum dolor sit amet</span>Ut enim ad minim veniam, quis nostrud exercitation ullamco laboris nisi ut aliquip ex ea commodo consequat. Duis aute irure dolor in reprehenderit in voluptate velit esse cillum dolore eu fugiat nulla pariatur.</div>
  <div class="abs body" style="left:189px;top:96px;width:70px"><span class="lead" style="margin-bottom:3px">Lorem ipsum dolor sit amet</span>Ut enim ad minim veniam, quis nostrud exercitation ullamco laboris nisi ut aliquip ex ea commodo consequat. Duis aute irure dolor in reprehenderit in voluptate velit esse cillum dolore eu fugiat nulla pariatur.</div>
  <div class="foot"><span class="brand"><i></i>COPPERLINE VENTURES</span><svg width="293" height="8" viewBox="0 0 293 8"><polygon points="218,8 226,2 293,2 293,8" fill="var(--blue)"/><rect y="6" width="293" height="2" fill="var(--red)"/></svg><span class="pg">02</span></div>
</section>

<!-- Services -->
<section class="slide c1 r3">
  <h2 class="slide-title">SERVICES</h2><p class="slide-sub">Subtitle goes here</p>
  <div class="svc" style="left:23px;top:46px"><div class="svc-head fill-blue"><svg width="12" height="12" viewBox="0 0 12 12" style="margin-bottom:3px"><path d="M6 1 L11 6 L6 11 L3 8 L6 6 L3 4 Z" fill="#fff"/></svg>MANAGEMENT<br>SOLUTIONS</div><div class="svc-body fill-grey">Dolor sit amet, consectetur adipiscing elit, sed do eiusmod tempor incididunt ut labore et dolore magna aliqua.</div></div>
  <div class="svc" style="left:84.5px;top:46px"><div class="svc-head fill-grey"><svg width="12" height="12" viewBox="0 0 12 12" style="margin-bottom:3px"><circle cx="6" cy="6" r="5" fill="none" stroke="#fff" stroke-width="1"/><rect x="5.4" y="5" width="1.2" height="4" fill="#fff"/><circle cx="6" cy="3.5" r=".7" fill="#fff"/></svg>INFORMATION<br>SOLUTIONS</div><div class="svc-body fill-blue">Dolor sit amet, consectetur adipiscing elit, sed do eiusmod tempor incididunt ut labore et dolore magna aliqua.</div></div>
  <div class="svc" style="left:146px;top:46px"><div class="svc-head fill-blue"><svg width="14" height="12" viewBox="0 0 14 12" style="margin-bottom:3px"><path d="M1 6 L5 3 L9 3 L13 6 L9 9 L5 9 Z" fill="#fff"/></svg>PROFESSIONAL<br>SERVICES</div><div class="svc-body fill-grey">Dolor sit amet, consectetur adipiscing elit, sed do eiusmod tempor incididunt ut labore et dolore magna aliqua.</div></div>
  <div class="svc" style="left:207.5px;top:46px"><div class="svc-head fill-grey"><svg width="12" height="12" viewBox="0 0 12 12" style="margin-bottom:3px"><circle cx="6" cy="6" r="1.6" fill="#fff"/><g stroke="#fff" stroke-width=".9"><line x1="6" y1="1" x2="6" y2="11"/><line x1="1" y1="6" x2="11" y2="6"/><line x1="2.5" y1="2.5" x2="9.5" y2="9.5"/></g></svg>ORGANIZATIONAL<br>TRANSFORMATION</div><div class="svc-body fill-blue">Dolor sit amet, consectetur adipiscing elit, sed do eiusmod tempor incididunt ut labore et dolore magna aliqua.</div></div>
  <div class="foot"><span class="brand"><i></i>COPPERLINE VENTURES</span><svg width="293" height="8" viewBox="0 0 293 8"><polygon points="218,8 226,2 293,2 293,8" fill="var(--blue)"/><rect y="6" width="293" height="2" fill="var(--red)"/></svg><span class="pg">02</span></div>
</section>

<!-- Solution -->
<section class="slide c2 r3">
  <h2 class="slide-title">SOLUTION</h2><p class="slide-sub">Subtitle goes here</p>
  <div class="abs" style="left:30px;top:41px;width:233px;text-align:center;font-size:3.4px;font-weight:700;font-style:italic;line-height:1.6">dolor sit amet, consectetur adipiscing elit, sed do eiusmod tempor incididunt ut labore et dolore magna aliqua.<br>Ut enim ad minim veniam, quis nostrud exercitation ullamco laboris nisi ut a</div>
  <div class="sol on" style="left:33px;top:63px"><b>⚙ Lorem ipsum dolor</b><span>Dolor sit amet, consectetur adipiscing elit, sed do eiusmod tempor incididunt ut labore et dolore magna aliqua.</span></div>
  <div class="sol off" style="left:111px;top:63px"><b>◔ Lorem ipsum dolor</b>Dolor sit amet, consectetur adipiscing elit, sed do eiusmod tempor incididunt ut labore et dolore magna aliqua.</div>
  <div class="sol on" style="left:190px;top:63px"><b>◆ Lorem ipsum dolor</b><span>Dolor sit amet, consectetur adipiscing elit, sed do eiusmod tempor incididunt ut labore et dolore magna aliqua.</span></div>
  <div class="sol off" style="left:33px;top:105px"><b>◷ Lorem ipsum dolor</b>Dolor sit amet, consectetur adipiscing elit, sed do eiusmod tempor incididunt ut labore et dolore magna aliqua.</div>
  <div class="sol on" style="left:111px;top:105px"><b>⚙ Lorem ipsum dolor</b><span>Dolor sit amet, consectetur adipiscing elit, sed do eiusmod tempor incididunt ut labore et dolore magna aliqua.</span></div>
  <div class="sol off" style="left:190px;top:105px"><b>▥ Lorem ipsum dolor</b>Dolor sit amet, consectetur adipiscing elit, sed do eiusmod tempor incididunt ut labore et dolore magna aliqua.</div>
  <div class="foot"><span class="brand"><i></i>COPPERLINE VENTURES</span><svg width="293" height="8" viewBox="0 0 293 8"><polygon points="218,8 226,2 293,2 293,8" fill="var(--blue)"/><rect y="6" width="293" height="2" fill="var(--red)"/></svg><span class="pg">02</span></div>
</section>

<!-- Bullet text -->
<section class="slide c3 r3">
  <h2 class="slide-title">BULLET TEXT</h2><p class="slide-sub">Subtitle goes here</p>
  <div class="bullet body" style="top:49px"><span class="lead">Lorem ipsum dolor sit amet</span>consectetur adipiscing elit, sed do eiusmod tempor incididunt ut labore et dolore magna aliqua. Ut enim ad minim veniam, quis nostrud exercitation ullamco laboris nisi ut aliquip ex ea commodo consequat. Duis aute irure dolor in reprehenderit in voluptate velit esse cillum dolore eu fugiat nulla.</div>
  <div class="bullet body" style="top:79px"><span class="lead">Lorem ipsum dolor sit amet</span>consectetur adipiscing elit, sed do eiusmod tempor incididunt ut labore et dolore magna aliqua. Ut enim ad minim veniam, quis nostrud exercitation ullamco laboris nisi ut aliquip ex ea commodo consequat. Duis aute irure dolor in reprehenderit in voluptate velit esse cillum dolore eu</div>
  <div class="bullet body" style="top:109px"><span class="lead">Lorem ipsum dolor sit amet</span>Excepteur sint occaecat cupidatat non proident, sunt in culpa qui officia deserunt mollit anim id est laborum. Excepteur sint occaecat cupidatat non proident, sunt in culpa. Duis aute irure dolor in reprehenderit in voluptate velit esse cillum dolore eu</div>
  <div class="foot"><span class="brand"><i></i>COPPERLINE VENTURES</span><svg width="293" height="8" viewBox="0 0 293 8"><polygon points="218,8 226,2 293,2 293,8" fill="var(--blue)"/><rect y="6" width="293" height="2" fill="var(--red)"/></svg><span class="pg">02</span></div>
</section>

<!-- Team -->
<section class="slide c1 r4">
  <h2 class="slide-title">TEAM</h2><p class="slide-sub">Subtitle goes here</p>
  <div class="member" style="left:18px;top:47px"><div class="avatar" role="img" aria-label="Portrait of team member"></div><div class="name">JORDAN VALE</div><div class="role">president</div><p class="body">dolor sit amet, consectetur adipiscing elit, sed do eiusmod tempor incididunt ut labore et dolore magna aliqua. Ut enim ad minim veniam, quis nostrud exercitation ullamco laboris nisi ut aliquip ex ea cillum dolore eu fugiat nulla pariatur.</p></div>
  <div class="member" style="left:115px;top:47px"><div class="avatar" role="img" aria-label="Portrait of team member"></div><div class="name">MINA HART</div><div class="role">CEO / Founder</div><p class="body">dolor sit amet, consectetur adipiscing elit, sed do eiusmod tempor incididunt ut labore et dolore magna aliqua. Ut enim ad minim veniam, quis nostrud exercitation ullamco laboris nisi ut aliquip ex ea cillum dolore eu fugiat nulla pariatur.</p></div>
  <div class="member" style="left:212px;top:47px"><div class="avatar" role="img" aria-label="Portrait of team member"></div><div class="name">NORA LEE</div><div class="role">vice president</div><p class="body">dolor sit amet, consectetur adipiscing elit, sed do eiusmod tempor incididunt ut labore et dolore magna aliqua. Ut enim ad minim veniam, quis nostrud exercitation ullamco laboris nisi ut aliquip ex ea cillum dolore eu fugiat nulla pariatur.</p></div>
  <div class="foot"><span class="brand"><i></i>COPPERLINE VENTURES</span><svg width="293" height="8" viewBox="0 0 293 8"><polygon points="218,8 226,2 293,2 293,8" fill="var(--blue)"/><rect y="6" width="293" height="2" fill="var(--red)"/></svg><span class="pg">02</span></div>
</section>

<!-- Chart: donuts -->
<section class="slide c2 r4">
  <h2 class="slide-title">OUR CHART</h2><p class="slide-sub">Subtitle goes here</p>
  <div class="donut" style="left:23px;top:55px">
    <svg width="40" height="40" viewBox="0 0 40 40"><circle cx="20" cy="20" r="16" fill="none" stroke="#9a9a9a" stroke-width="4"/><circle cx="20" cy="20" r="16" fill="none" stroke="var(--red)" stroke-width="4" stroke-dasharray="81.4 100.5" transform="rotate(-90 20 20)"/><text x="20" y="22.5" text-anchor="middle" font-size="7" font-weight="700" fill="var(--blue)" font-family="Roboto,sans-serif">81%</text></svg>
    <p class="body">dolor sit amet, consectetur adipiscing elit, sed do eiusmod tempor incididunt ut labore et dolore magna aliqua. Ut enim ad minim veniam, quis nostrud exercitation ullamco laboris nisi ut aliquip ex ea cillum dolore eu fugiat nulla pariatur.</p></div>
  <div class="donut" style="left:115px;top:55px">
    <svg width="40" height="40" viewBox="0 0 40 40"><circle cx="20" cy="20" r="16" fill="none" stroke="var(--blue)" stroke-width="4"/><circle cx="20" cy="20" r="16" fill="none" stroke="var(--red)" stroke-width="4" stroke-dasharray="72.4 100.5" transform="rotate(-90 20 20)" opacity="0"/><circle cx="20" cy="20" r="16" fill="none" stroke="#9a9a9a" stroke-width="4" stroke-dasharray="28.1 100.5" transform="rotate(170 20 20)"/><text x="20" y="22.5" text-anchor="middle" font-size="7" font-weight="700" fill="var(--blue)" font-family="Roboto,sans-serif">72%</text></svg>
    <p class="body">dolor sit amet, consectetur adipiscing elit, sed do eiusmod tempor incididunt ut labore et dolore magna aliqua. Ut enim ad minim veniam, quis nostrud exercitation ullamco laboris nisi ut aliquip ex ea cillum dolore eu fugiat nulla pariatur.</p></div>
  <div class="donut" style="left:207px;top:55px">
    <svg width="40" height="40" viewBox="0 0 40 40"><circle cx="20" cy="20" r="16" fill="none" stroke="#9a9a9a" stroke-width="4"/><circle cx="20" cy="20" r="16" fill="none" stroke="var(--red)" stroke-width="4" stroke-dasharray="63.3 100.5" transform="rotate(-90 20 20)"/><text x="20" y="22.5" text-anchor="middle" font-size="7" font-weight="700" fill="var(--blue)" font-family="Roboto,sans-serif">63%</text></svg>
    <p class="body">dolor sit amet, consectetur adipiscing elit, sed do eiusmod tempor incididunt ut labore et dolore magna aliqua. Ut enim ad minim veniam, quis nostrud exercitation ullamco laboris nisi ut aliquip ex ea cillum dolore eu fugiat nulla pariatur.</p></div>
  <div class="foot"><span class="brand"><i></i>COPPERLINE VENTURES</span><svg width="293" height="8" viewBox="0 0 293 8"><polygon points="218,8 226,2 293,2 293,8" fill="var(--blue)"/><rect y="6" width="293" height="2" fill="var(--red)"/></svg><span class="pg">02</span></div>
</section>

<!-- Chart: bars -->
<section class="slide c3 r4">
  <h2 class="slide-title">OUR CHART</h2><p class="slide-sub">Subtitle goes here</p>
  <div class="abs body" style="left:27px;top:55px;width:133px"><span class="lead">Lorem ipsum dolor sit amet</span>consectetur adipiscing elit, sed do eiusmod tempor incididunt ut labore et dolore magna aliqua. Ut enim ad minim veniam, quis nostrud exercitation ullamco laboris nisi ut aliquip ex ea commodo consequat. Duis aute irure dolor in reprehenderit in voluptate velit esse cillum dolore eu fugiat nulla pariatur.<br><span class="lead" style="margin-top:4px">Lorem ipsum dolor sit amet</span>consectetur adipiscing elit, sed do eiusmod tempor incididunt ut labore et dolore magna aliqua. Ut enim ad minim veniam, quis nostrud exercitation ullamco laboris nisi ut aliquip ex ea commodo consequat. Duis aute irure dolor in reprehenderit in voluptate velit esse cillum dolore eu</div>
  <svg class="abs" style="left:182px;top:44px" width="80" height="50" viewBox="0 0 80 50">
    <line x1="0" y1="42" x2="80" y2="42" stroke="#bbb" stroke-width=".5"/>
    <rect x="5" y="6" width="4" height="36" fill="var(--blue)"/><rect x="9" y="28" width="4" height="14" fill="var(--red)"/><rect x="13" y="32" width="4" height="10" fill="#9a9a9a"/>
    <rect x="24" y="18" width="4" height="24" fill="var(--blue)"/><rect x="28" y="24" width="4" height="18" fill="var(--red)"/><rect x="32" y="8" width="4" height="34" fill="#9a9a9a"/>
    <rect x="43" y="8" width="4" height="34" fill="var(--blue)"/><rect x="47" y="20" width="4" height="22" fill="var(--red)"/><rect x="51" y="30" width="4" height="12" fill="#9a9a9a"/>
    <rect x="62" y="12" width="4" height="30" fill="var(--blue)"/><rect x="66" y="26" width="4" height="16" fill="#9a9a9a"/><rect x="70" y="8" width="4" height="34" fill="var(--red)"/>
    <g font-size="2.6" fill="#555" font-family="Roboto,sans-serif" text-anchor="middle"><text x="11" y="47">2009</text><text x="30" y="47">2010</text><text x="49" y="47">2011</text><text x="68" y="47">2012</text></g>
  </svg>
  <div class="abs" style="left:210px;top:103px;font-size:2.8px;line-height:1.35;width:40px"><span style="display:inline-block;width:3px;height:3px;background:var(--blue);margin-right:2px"></span><b>LOREM IPSUM</b><br>Lorem ipsum dolor sit amet consectetur adipiscing elit sed do eiusmod</div>
  <div class="abs" style="left:210px;top:120px;font-size:2.8px;line-height:1.35;width:40px"><span style="display:inline-block;width:3px;height:3px;background:var(--red);margin-right:2px"></span><b>LOREM IPSUM</b><br>Lorem ipsum dolor sit amet consectetur adipiscing elit sed do eiusmod</div>
  <div class="foot"><span class="brand"><i></i>COPPERLINE VENTURES</span><svg width="293" height="8" viewBox="0 0 293 8"><polygon points="218,8 226,2 293,2 293,8" fill="var(--blue)"/><rect y="6" width="293" height="2" fill="var(--red)"/></svg><span class="pg">02</span></div>
</section>

<!-- Section divider -->
<section class="slide c1 r5" style="background:var(--blue)">
  <div class="photo" role="img" aria-label="Faint floating data cubes over blue" style="inset:0;background:radial-gradient(circle at 75% 45%,rgba(255,255,255,.25),transparent 50%),radial-gradient(circle at 15% 20%,rgba(255,255,255,.15),transparent 40%),linear-gradient(135deg,#2a73cc,var(--blue-dark))"></div>
  <div class="abs" style="left:130px;top:68px;width:34px;height:34px;border-radius:50%;background:var(--white);display:flex;align-items:center;justify-content:center"><div style="width:29px;height:29px;border-radius:50%;background:var(--red);color:var(--white);display:flex;align-items:center;justify-content:center;font-family:Georgia,serif;font-style:italic;font-weight:700;font-size:18px">i</div></div>
  <div class="abs" style="left:78px;top:107px;width:137px;height:.6px;background:rgba(255,255,255,.6)"></div>
  <div class="abs heading-white" style="left:0;top:113px;width:293px;text-align:center;font-size:9px;font-weight:300">SECTION TITLE</div>
</section>

<!-- Image text -->
<section class="slide c2 r5">
  <div class="abs" style="left:0;top:0;width:142px;height:166px;background:var(--blue)"></div>
  <div class="abs heading-white" style="left:12px;top:12px"><div style="font-size:8.5px;font-weight:300">IMAGE TEXT</div><div style="font-size:3.6px;margin-top:2px">SUBTITLE GOES HERE</div></div>
  <div class="abs heading-white" style="left:17px;top:55px;width:110px;font-size:3.4px;font-weight:700;line-height:1.65;text-align:justify">Lorem ipsum dolor sit amet, consectetur adipiscing elit, sed do eiusmod tempor incididunt ut labore et dolore magna aliqua. Ut enim ad minim veniam, quis nostrud exercitation ullamco laboris nisi ut aliquip ex ea commodo consequat. Duis aute irure dolor in reprehenderit in voluptate velit esse cillum dolore eu fugiat nulla pariatur.<br><br>Lorem ipsum dolor sit amet, consectetur adipiscing elit, sed do eiusmod tempor incididunt ut labore et dolore</div>
  <div class="brand abs" style="left:7px;top:151px;font-size:3.4px;color:var(--white)"><i style="width:5px;height:5px;margin-right:2px;background:var(--white)"></i>COPPERLINE VENTURES</div>
  <div class="photo" role="img" aria-label="Two smiling colleagues, black and white portrait" style="left:142px;top:0;width:151px;height:166px;background:linear-gradient(135deg,#f4f4f4,#9c9c9c 60%,#3a3a3a)"></div>
</section>

<!-- Thank you -->
<section class="slide c3 r5">
  <div class="brand abs" style="left:30px;top:35px;font-size:5px"><i style="width:11px;height:11px;margin-right:3px"></i>COPPERLINE<br>VENTURES</div>
  <svg class="abs" style="left:0;top:52px" width="293" height="114" viewBox="0 0 293 114">
    <path d="M0 32 L90 32 C120 32 125 0 160 0 L293 0 L293 114 L0 114 Z" fill="var(--blue)"/>
  </svg>
  <div class="photo" role="img" aria-label="Close-up of an eye with binary code overlay" style="left:150px;top:52px;width:143px;height:110px;background:radial-gradient(ellipse at 55% 45%,rgba(210,225,245,.55),rgba(10,98,196,0) 65%)"></div>
  <div class="abs heading-white" style="left:28px;top:107px"><div style="font-size:6px;font-weight:900;letter-spacing:-.3px">THANK YOU</div><div style="font-size:7px;font-weight:300">FOR YOUR TIME</div></div>
  <div class="contact" style="top:124px"><i></i>742 Alder Loop Ste 310</div>
  <div class="contact" style="top:136px"><i></i>support@copperline.example</div>
  <div class="contact" style="top:148px"><i></i>www.copperline.example</div>
  <div class="abs" style="left:0;bottom:0;width:293px;height:3px;background:var(--red)"></div>
</section>

</main>
</body>
</html>
```